Web Design Project - Investor Services

I would like a simple and elegant web design for my company "Torvelo Management". The company will provide services to Corporate and Institutional investors for their needs with local/foreign investment vehicles. The website will have four pages to start: home, about us, services, contact.
I already chose a logo, and I will attach the source file. The color that I will most probably use for the logo will be blue, and i also like grey with a white background. For the website I would like to see light colors, maybe light green or grey, with the logo either in blue, grey or white (depeding on the background).
Target Market(s)
Investment managers and tax/legal advisors from top firms. This is the reason why I want something simple and elegant.
Industry/Entity Type
Investment
Requirements
Nice to have
- I do not want many pictures in the website, but I might include a couple of pictures of Madrid and maybe a picture of myself in the about us page (still deciding). I will attach some pictures of Madrid that I like, but feel free to search for others - i have others but i am not able to attach all of them.

```html
<!DOCTYPE html>
<html lang="en">
<head>
<meta charset="utf-8">
<title>Torvelo Management</title>
<link href="https://fonts.googleapis.com/css2?family=Lato:wght@400;700&family=Arimo:wght@400&display=swap" rel="stylesheet">
<style>
:root{
  --brand:#1a1f7a;
  --heading:#2f3c8e;
  --nav-top:#5c68b4;
  --nav-bottom:#2f3a86;
  --nav-active:#7079be;
  --text:#5a5a5a;
  --muted:#6a6a6a;
  --rule:#dcdcdc;
  --button:#5b5b5b;
  --white:#ffffff;
}
*{margin:0;padding:0;box-sizing:border-box}
html,body{width:1200px;height:1148px;overflow:hidden}
body{position:relative;background:linear-gradient(#ececec 556px,#f6f6f6 700px,#ffffff 900px);font-family:"Arimo",Arial,sans-serif;color:var(--text)}
.header{position:absolute;left:0;top:0;width:1200px;height:102px;background:var(--white)}
.logo{position:absolute;left:90px;top:28px;display:flex;align-items:center;gap:12px;font-family:"Lato",sans-serif;font-size:34px;color:var(--brand);font-weight:400;letter-spacing:.5px}
.logo-mark{width:14px;height:14px;background:var(--brand)}
.search{position:absolute;left:943px;top:37px;width:169px;height:28px;border:1px solid #cfcfcf;background:#f7f7f7;font-size:11px;color:#333;padding:7px 12px}
.search svg{position:absolute;right:8px;top:5px}
.nav{position:absolute;left:0;top:102px;width:1200px;height:55px;background:linear-gradient(var(--nav-top),var(--nav-bottom));box-shadow:0 3px 4px rgba(0,0,0,.35);font-family:"Lato",sans-serif;color:var(--white);font-size:15px}
.nav-item{position:absolute;top:0;height:52px;line-height:52px;text-align:center;border-right:1px solid #26306f}
.nav-item.active{background:var(--nav-active)}
.nav-first{border-left:1px solid #26306f}
.nav-contact{position:absolute;right:88px;top:0;line-height:52px;font-size:14.5px}
.nav-contact span{margin:0 12px}
.hero{position:absolute;left:0;top:157px;width:1200px;height:399px;background:linear-gradient(90deg,#c9807a 0%,#e3aaa2 20%,#f0b8b0 50%,#e4aaa2 80%,#c37a74 100%)}
.hero-arrow{position:absolute;top:173px;width:42px;height:42px;border-radius:50%;background:rgba(255,255,255,.8)}
.caption{position:absolute;left:317px;top:299px;width:567px;height:50px;background:rgba(40,30,35,.85);color:var(--white);font-family:"Lato",sans-serif;font-size:20px;line-height:50px;text-align:center}
.content{position:absolute;left:90px;top:524px;width:1022px;height:624px;background:var(--white)}
.welcome-title{position:absolute;left:10px;top:16px;font-family:"Lato",sans-serif;font-weight:400;font-size:22px;color:var(--heading)}
.welcome-text{position:absolute;left:10px;top:53px;width:694px;font-size:13.5px;line-height:23px;color:var(--text)}
.welcome-photo{position:absolute;left:718px;top:23px;width:295px;height:138px;border:6px solid #eeeeee;background:linear-gradient(90deg,#f4f4f4,#e7ece6 50%,#f2f2f2)}
.rule{position:absolute;left:7px;width:1006px;height:1px;background:var(--rule)}
.service{position:absolute;top:220px;width:310px}
.service h2{font-family:"Lato",sans-serif;font-weight:400;font-size:20px;color:var(--heading)}
.service-photo{margin-top:13px;width:307px;height:148px;border:1px solid #e0e0e0;padding:6px}
.service-photo div{width:100%;height:100%}
.service p{margin-top:18px;font-size:13px;line-height:23px;color:var(--muted);text-align:justify}
.button{display:inline-block;margin-top:13px;width:86px;height:29px;line-height:29px;text-align:center;background:var(--button);border-radius:3px;color:var(--white);font-size:13px}
.footer-links{position:absolute;left:7px;top:558px;font-size:12.5px;color:var(--muted)}
.footer-links span{margin:0 9px}
.copyright{position:absolute;left:7px;top:590px;font-size:12.5px;color:var(--muted);word-spacing:2px}
.social{position:absolute;top:570px;width:25px;height:25px;border-radius:3px}
</style>
</head>
<body>
<header class="header">
  <div class="logo"><span class="logo-mark"></span>Torvelo Management</div>
  <div class="search">Search
    <svg width="16" height="16" viewBox="0 0 16 16"><circle cx="6" cy="6" r="4.5" fill="#333"/><line x1="9" y1="9" x2="14" y2="14" stroke="#333" stroke-width="3" stroke-linecap="round"/></svg>
  </div>
</header>

<nav class="nav">
  <div class="nav-item nav-first active" style="left:90px;width:94px">Home</div>
  <div class="nav-item" style="left:184px;width:113px">About us</div>
  <div class="nav-item" style="left:297px;width:105px">Services</div>
  <div class="nav-item" style="left:402px;width:108px">Contact</div>
  <div class="nav-contact">Call us : 555 210 4470<span>|</span>E-mail : info@torvelomanagement.com</div>
</nav>

<section class="hero" role="img" aria-label="Madrid skyline with tall office towers at dusk under a pink sky">
  <div class="hero-arrow" style="left:90px"><svg width="42" height="42" viewBox="0 0 42 42"><polyline points="24,13 16,21 24,29" fill="none" stroke="#888" stroke-width="1.6"/></svg></div>
  <div class="hero-arrow" style="left:1070px"><svg width="42" height="42" viewBox="0 0 42 42"><polyline points="18,13 26,21 18,29" fill="none" stroke="#888" stroke-width="1.6"/></svg></div>
  <div class="caption">We provide services to Corporate and Institutional investors</div>
</section>

<main class="content">
  <h1 class="welcome-title">Welcome to our site</h1>
  <p class="welcome-text">Proin tincidunt ipsum non nunc porttitor imperdiet sagittis lectus accumsan. Proin ac nibh eget dolor pulvinar tincidunt non condimentum nisl. Class aptent taciti sociosqu ad litora torquent per conubia nostra, per inceptos himenaeos. Sed massa enim, sodales id dignissim mollis, adipiscing a neque. Proin pulvinar dictum volutpat. Donec erat mauris, ornare quis gravida at, dignissim sed neque. Pellentesque metus risus, mattis a ullamcorper vitae, iaculis quis quam. Mauris mi lorem, rutrum non mollis porta, faucibus at tellus.</p>
  <div class="welcome-photo" role="img" aria-label="Businessman watering small potted plants on a desk"></div>

  <div class="rule" style="top:188px"></div>

  <article class="service" style="left:11px">
    <h2>Local Investments</h2>
    <div class="service-photo"><div role="img" aria-label="Business team reviewing documents at a table" style="background:linear-gradient(90deg,#9fb2cc,#2c3f66 50%,#d8dfe8)"></div></div>
    <p>Pellentesque metus risus, mattis a ullamcorper vitae, iaculis quis quam. Mauris mi lorem, rutrum non mollis porta, faucibus at tellus.</p>
    <span class="button">View more</span>
  </article>

  <article class="service" style="left:358px">
    <h2>Foreign Investments</h2>
    <div class="service-photo"><div role="img" aria-label="Two businessmen shaking hands" style="background:linear-gradient(90deg,#1e2230,#d9a88c 45%,#c8d4dc 70%,#6f7480)"></div></div>
    <p>Pellentesque metus risus, mattis a ullamcorper vitae, iaculis quis quam. Mauris mi lorem, rutrum non mollis porta, faucibus at tellus.</p>
    <span class="button">View more</span>
  </article>

  <article class="service" style="left:704px">
    <h2>Investments Consultation</h2>
    <div class="service-photo"><div role="img" aria-label="Desktop monitor showing financial charts" style="background:linear-gradient(90deg,#f3f3f3,#d8d8d8 40%,#ececec)"></div></div>
    <p>Pellentesque metus risus, mattis a ullamcorper vitae, iaculis quis quam. Mauris mi lorem, rutrum non mollis porta, faucibus at tellus.</p>
    <span class="button">View more</span>
  </article>

  <div class="rule" style="top:542px"></div>

  <div class="footer-links">Home<span>|</span>About us,<span>|</span>Services<span>|</span>Contact</div>
  <div class="copyright">Copyright &copy; 2013 &nbsp;www.torvelomanagement.com &nbsp;All rights reserved.</div>
  <div class="social" style="left:958px;background:#3b5a9a" aria-label="Social link"></div>
  <div class="social" style="left:989px;background:#3aa9dc" aria-label="Social link"></div>
</main>
</body>
</html>
```